KORVELLA Corporate Business Card

Modern business card design for company which focuses in the areas of Staffing, IT Consulting & Data Services. Please note: We are no longer using the IT subscript on the logo. All designs should have IT subscript removed.
Website: www.korvellait.example

```html
<!DOCTYPE html>
<html lang="en">
<head>
<meta charset="UTF-8">
<title>KORVELLA Business Card</title>
<link rel="stylesheet" href="https://fonts.googleapis.com/css2?family=Montserrat:wght@600;700&family=Lato:wght@400;700&display=swap">
<style>
  :root {
    --navy: #055a96;
    --sky: #1e9ad6;
    --paper: #ffffff;
    --ink: #4a4a4a;
    --backdrop: #2b2e34;
  }
  * { margin: 0; padding: 0; box-sizing: border-box; }
  html, body { width: 1200px; height: 1000px; overflow: hidden; }
  body {
    background: var(--backdrop);
    position: relative;
    font-family: 'Lato', sans-serif;
  }
  .card {
    position: absolute;
    left: 215px;
    width: 770px;
    height: 440px;
    border-radius: 24px;
    overflow: hidden;
    box-shadow: 0 14px 30px rgba(0,0,0,0.45);
  }
  .card--front { top: 40px; background: var(--navy); }
  .card--back { top: 520px; background: var(--paper); }

  .front-wordmark {
    position: absolute;
    inset: 0;
    display: flex;
    align-items: center;
    justify-content: center;
    font-family: 'Montserrat', sans-serif;
    font-weight: 700;
    font-size: 86px;
    letter-spacing: 2px;
    color: var(--paper);
  }

  .back-wordmark {
    position: absolute;
    left: 48px;
    top: 150px;
    font-family: 'Montserrat', sans-serif;
    font-weight: 700;
    font-size: 50px;
    letter-spacing: 1px;
    color: var(--sky);
  }
  .divider {
    position: absolute;
    left: 385px;
    top: 110px;
    width: 2px;
    height: 195px;
    background: var(--sky);
  }
  .contact-block {
    position: absolute;
    left: 412px;
    top: 108px;
    color: var(--ink);
    font-size: 17px;
    line-height: 1.3;
  }
  .contact-name {
    font-family: 'Montserrat', sans-serif;
    font-weight: 700;
    font-size: 27px;
    letter-spacing: 1px;
    color: var(--sky);
    margin-bottom: 2px;
  }
  .contact-title { margin-bottom: 8px; }
  .contact-address { margin-bottom: 10px; }
  .contact-list { list-style: none; }
  .contact-list li {
    display: flex;
    align-items: center;
    gap: 10px;
    margin-bottom: 5px;
  }
  .contact-list svg { width: 15px; height: 15px; flex: none; }
  .wave { position: absolute; left: 0; bottom: 0; width: 770px; height: 440px; }
</style>
</head>
<body>
  <section class="card card--front">
    <div class="front-wordmark">KORVELLA</div>
  </section>

  <section class="card card--back">
    <svg class="wave" viewBox="0 0 770 440" aria-hidden="true">
      <path d="M0,300 C150,375 300,392 450,397 C600,402 700,368 770,350 L770,440 L0,440 Z" fill="var(--sky)"/>
      <path d="M0,316 C150,390 300,402 450,407 C600,412 700,380 770,364 L770,440 L0,440 Z" fill="var(--navy)" stroke="var(--paper)" stroke-width="3"/>
    </svg>

    <div class="back-wordmark">KORVELLA</div>
    <div class="divider"></div>

    <div class="contact-block">
      <p class="contact-name">Dorian Ashford</p>
      <p class="contact-title">Managing Director</p>
      <p class="contact-address">418 Calloway St.<br>Brennington, OH 45099</p>
      <ul class="contact-list">
        <li>
          <svg viewBox="0 0 24 24"><path fill="var(--navy)" d="M6.6 10.8a15.1 15.1 0 0 0 6.6 6.6l2.2-2.2a1 1 0 0 1 1-.25 11.4 11.4 0 0 0 3.6.57 1 1 0 0 1 1 1V20a1 1 0 0 1-1 1A17 17 0 0 1 3 4a1 1 0 0 1 1-1h3.5a1 1 0 0 1 1 1c0 1.25.2 2.45.57 3.57a1 1 0 0 1-.25 1z"/></svg>
          555-014-2736
        </li>
        <li>
          <svg viewBox="0 0 24 24"><rect x="2" y="5" width="20" height="14" rx="2" fill="none" stroke="var(--navy)" stroke-width="2.5"/><path d="M3 6l9 7 9-7" fill="none" stroke="var(--navy)" stroke-width="2.5"/></svg>
          contactus@korvellait.example
        </li>
        <li>
          <svg viewBox="0 0 24 24"><circle cx="12" cy="12" r="10" fill="none" stroke="var(--navy)" stroke-width="2.5"/><path d="M2 12h20M12 2c3 3 3 17 0 20M12 2c-3 3-3 17 0 20" fill="none" stroke="var(--navy)" stroke-width="1.8"/></svg>
          www.korvellait.example
        </li>
      </ul>
    </div>
  </section>
</body>
</html>
```